Fresh Tarrow Work Post - Business Card Required

Dear All,

I own Velmira Limited, which in turn owns the website:
www.harbinworkpost.example

I want all of you wonderful creative people to come up with a slick, and awesome business card design that incorporates the logo on the site, and some colouring and design elements from it.

You have free reign in how you go about doing this, I won't be giving my contact details on this platform, but the winner will be asked to redesign based on my contact details which I will supply at the end.

I need the design to be completed within 5 days. I need the final print copies of the business cards by the 25th November, so unfortunately it's a bit of a rush to get these designs ready.

Any questions, please ask.

Thank you
Updates

Thank you all for your hard work and exceptional designs provided. I do have to pick one, so I have a very clear idea of which one this is, however I will wait one further day until the competition closes to be fair to all those have submitted, or are in the process of submitting. I wish you all the best and thank you again for your dedication.

```html
<!DOCTYPE html>
<html lang="en">
<head>
<meta charset="utf-8">
<title>Harbin Workpost – Business Card</title>
<link href="https://fonts.googleapis.com/css2?family=Didact+Gothic&display=swap" rel="stylesheet">
<style>
  :root {
    --stage-dark: #3e3e3e;
    --stage-light: #8a8a8a;
    --cream: #efe3d1;
    --cream-light: #f8f1e6;
    --gold-deep: #b07a1e;
    --gold-mid: #d7a449;
    --gold-light: #f3d68e;
    --gold-text: #b5862e;
    --ink: #1f1f1f;
    --rule: #b8a888;
    --white: #ffffff;
  }
  * { box-sizing: border-box; margin: 0; padding: 0; }
  html, body { width: 1200px; height: 877px; overflow: hidden; }
  body {
    font-family: "Didact Gothic", "Century Gothic", sans-serif;
    background: radial-gradient(ellipse at 50% 50%, var(--stage-light) 0%, var(--stage-dark) 75%);
    position: relative;
  }
  .card {
    position: absolute;
    left: 253px;
    width: 659px;
    height: 357px;
    border-radius: 11px;
    overflow: hidden;
    box-shadow: 0 4px 10px rgba(0,0,0,0.45);
  }
  .card--front {
    top: 68px;
    background: radial-gradient(circle at 50% 48%, var(--cream-light) 0%, var(--cream) 55%);
  }
  .card--back { top: 485px; background: var(--white); }

  .band {
    position: absolute; left: 0; right: 0; height: 33px;
    background: linear-gradient(90deg, var(--gold-deep) 0%, var(--gold-mid) 30%, var(--gold-light) 55%, var(--gold-mid) 80%, var(--gold-deep) 100%);
  }
  .band--top { top: 0; }
  .band--bottom {
    bottom: 0;
    display: flex; align-items: center; justify-content: center;
    color: var(--white); font-size: 16px; letter-spacing: 1.2px;
  }

  .brand-name {
    position: absolute; color: var(--gold-text);
    letter-spacing: 3px; text-transform: uppercase; white-space: nowrap;
    display: flex; align-items: center; gap: 10px;
  }
  .brand-name .brand-dot {
    width: 10px; height: 10px; border-radius: 50%; background: var(--gold-text);
  }
  .card--front .brand-name {
    top: 50%; left: 50%; transform: translate(-50%, -50%);
    font-size: 28px;
  }
  .card--back .brand-name {
    top: 78px; left: 526px; transform: translateX(-50%);
    font-size: 14px; letter-spacing: 2px; gap: 6px;
  }
  .card--back .brand-name .brand-dot { width: 7px; height: 7px; }

  .contact { position: absolute; left: 136px; top: 76px; color: var(--ink); }
  .contact__name { font-size: 29px; letter-spacing: 1px; line-height: 1.1; }
  .contact__title { font-size: 16px; letter-spacing: 0.6px; margin-top: 3px; }
  .contact__rule {
    width: 306px; height: 1px; background: var(--rule);
    margin: 8px 0 9px -13px;
  }
  .contact__details { font-size: 15.5px; letter-spacing: 0.8px; line-height: 21px; }
  .contact__details p + p { margin-top: 2px; }
  .contact__address { margin-bottom: 1px; }

  .gold-sweep { position: absolute; left: 0; top: 0; }
</style>
</head>
<body>
  <section class="card card--front" aria-label="Card front">
    <div class="band band--top"></div>
    <div class="brand-name"><span class="brand-dot"></span>Harbin Workpost</div>
    <div class="band band--bottom">www.harbinworkpost.example</div>
  </section>

  <section class="card card--back" aria-label="Card back">
    <svg class="gold-sweep" width="659" height="357" viewBox="0 0 659 357" aria-hidden="true">
      <defs>
        <linearGradient id="sweepGold" x1="0" y1="1" x2="1" y2="0">
          <stop offset="0" stop-color="#f6e2b0"/>
          <stop offset="0.45" stop-color="#c48b2c"/>
          <stop offset="0.7" stop-color="#f0d08a"/>
          <stop offset="1" stop-color="#a9721c"/>
        </linearGradient>
      </defs>
      <path d="M300 357 C 470 340, 610 300, 659 200 L 659 357 Z" fill="url(#sweepGold)"/>
      <path d="M270 357 C 450 332, 600 290, 659 182" fill="none" stroke="#d9b166" stroke-width="2"/>
    </svg>

    <div class="contact">
      <h1 class="contact__name">Tamsin Orrell</h1>
      <p class="contact__title">Managing Director</p>
      <div class="contact__rule"></div>
      <div class="contact__details">
        <p class="contact__address">12 Wrenfield Row,<br>Carlow Vale, London,<br>E9 4QT</p>
        <p>0700 900 4182</p>
        <p>contact@harbinworkpost.example</p>
        <p>www.harbinworkpost.example</p>
      </div>
    </div>

    <div class="brand-name"><span class="brand-dot"></span>Harbin Workpost</div>
  </section>
</body>
</html>
```